Business Card Design for New Game Studio

We need a business card design. We are a new company developing innovative mobile and platform games.

I would like to see very innovative design thats brings out the company's goal and direction.

My Company's goal and direction is to "Evolve the way of gaming, Bring fun and entertainment to all gamers"

Please do use our company logo which I have attached to be included in the design.

Please put in details for name, title, contacts etc ... be creative !!!

Reason: Company logo redesign. Awaiting it. Thanks

Hi all Please do wait for my updated company logo. Thanks

Reason: Still waiting on new company logo. Thanks all

Hi All Designers .... Sorry for the long wait... Please see the new file for my new company logo uploaded. Waiting to see all your creative design. Cheers

Hi All .... Please do not just mass send a whole bunch of similar designs .... Would like to see quality instead of quantity Cheers

Entertainment

```html
<!DOCTYPE html>
<html lang="en">
<head>
<meta charset="utf-8">
<title>Kestrel Play – Business Card</title>
<link rel="stylesheet" href="https://fonts.googleapis.com/css2?family=Graduate&family=Exo+2:wght@500;700&display=swap">
<style>
  :root {
    --stage: #2b2b2b;
    --navy: #29297f;
    --lime: #cfdc1e;
    --name-font: "Graduate", serif;
    --text-font: "Exo 2", sans-serif;
  }
  html, body {
    margin: 0;
    width: 1200px;
    height: 900px;
    overflow: hidden;
    background: var(--stage);
  }
  .canvas {
    position: relative;
    width: 1200px;
    height: 900px;
  }
  .card {
    position: absolute;
    background: var(--lime);
    overflow: hidden;
    box-shadow: 0 18px 40px rgba(0,0,0,.45);
  }
  .card-shape {
    position: absolute;
    inset: 0;
    width: 100%;
    height: 100%;
  }
  .card-shape path { fill: var(--navy); }

  /* Front: portrait */
  .card-front { left: 80px; top: 135px; width: 360px; height: 630px; }
  .company-name {
    position: absolute; top: 48px; right: 30px; margin: 0;
    font: 400 34px/1 var(--name-font);
    color: var(--lime); font-variant: small-caps;
  }
  .brand {
    position: absolute;
    display: flex; align-items: center; gap: 10px;
    font: 700 28px/1 var(--text-font);
    color: var(--lime);
  }
  .brand-dot { width: 14px; height: 14px; border-radius: 50%; background: var(--lime); }
  .card-front .brand { top: 230px; left: 40px; }
  .person { position: absolute; right: 30px; bottom: 48px; text-align: right; color: var(--navy); }
  .person-name { margin: 0; font: 400 38px/1.1 var(--name-font); font-variant: small-caps; }
  .person-title { margin: 4px 0 0; font: 400 24px/1 var(--name-font); text-transform: uppercase; }

  /* Back: landscape */
  .card-back { left: 500px; top: 270px; width: 630px; height: 360px; }
  .back-name {
    position: absolute; top: 26px; left: 30px; margin: 0;
    font: 400 32px/1 var(--name-font); color: var(--navy); font-variant: small-caps;
  }
  .tagline {
    position: absolute; top: 82px; left: 110px; margin: 0;
    font: 500 14px/1.5 var(--text-font); color: var(--navy);
    font-variant: small-caps; letter-spacing: .5px; text-align: right;
  }
  .contacts {
    position: absolute; top: 150px; left: 30px; margin: 0; padding: 0; list-style: none;
    font: 500 17px/1.5 var(--text-font); color: var(--navy);
  }
  .contacts li { display: flex; align-items: center; gap: 10px; }
  .contacts svg { width: 14px; height: 14px; }
  .icon-line { fill: none; stroke: var(--navy); stroke-width: 1.6; }
  .icon-fill { fill: var(--navy); }
  .card-back .brand { right: 30px; bottom: 40px; }
</style>
</head>
<body>
<main class="canvas">

  <section class="card card-front" aria-label="Business card front">
    <svg class="card-shape" viewBox="0 0 360 630" preserveAspectRatio="none" aria-hidden="true">
      <path d="M0 0 H360 V400 C250 400 140 480 0 380 Z"/>
    </svg>
    <h1 class="company-name">Company Name</h1>
    <div class="brand"><span class="brand-dot"></span>Kestrel Play</div>
    <div class="person">
      <p class="person-name">Your Name</p>
      <p class="person-title">Title</p>
    </div>
  </section>

  <section class="card card-back" aria-label="Business card back">
    <svg class="card-shape" viewBox="0 0 630 360" preserveAspectRatio="none" aria-hidden="true">
      <path d="M630 60 C450 90 350 300 140 360 H630 Z"/>
    </svg>
    <h2 class="back-name">Your Name</h2>
    <p class="tagline">Evolve the way of gaming<br>Bring fun and entertainment to all gamers</p>
    <ul class="contacts">
      <li><svg viewBox="0 0 16 16"><circle class="icon-line" cx="8" cy="8" r="6.5"/></svg>www.yourwebsite.com</li>
      <li><svg viewBox="0 0 16 16"><path class="icon-line" d="M1 3h14v10H1z M1 3l7 6 7-6"/></svg>youremail@website.com</li>
      <li><svg viewBox="0 0 16 16"><path class="icon-fill" d="M2 5c0-2 2-3 6-3s6 1 6 3v2h-3V5H5v2H2z M4 8h8l2 6H2z"/></svg>your phone Number</li>
    </ul>
    <div class="brand"><span class="brand-dot"></span>Kestrel Play</div>
  </section>

</main>
</body>
</html>
```